American cannabis tech company business card design

Thrum.com is seeking a modern, professional, and brand-aligned business card that represents our company and its core values: Mission, Story, Values, and Impact. As an innovative cannabis company, we want a business card that is not only visually appealing but also serves as a representation of who we are and what we stand for.

Project Scope: Design a double-sided business card that integrates our brand identity and core values. Incorporate our key brand elements, ensuring a sleek and contemporary aesthetic. Visually reflect our core values (Mission, Story, Values, Impact) in a way that is engaging yet professional.

Target Market(s)

Vendors, third parties,

Contact Information for Business Card

Contact details (name, title, email, phone, website, etc.)

Font styles to use
Other font styles liked:
• Caslon, Centra

Colors

Designer to choose colors to be used in the design.

Requirements
Must have
• Thrum.com logo and branding A creative yet clean way to integrate our core values (Mission, Story, Values, Impact) Modern typography and a well-structured layout
Nice to have
• forest green, grey, white, black
Should not have
• references to marijuana, leafs, plants, or related product

```html
<!DOCTYPE html>
<html lang="en">
<head>
<meta charset="utf-8">
<title>Thrum.com Business Card</title>
<link href="https://fonts.googleapis.com/css2?family=Poppins:wght@400;500;700&display=swap" rel="stylesheet">
<style>
  :root {
    --canvas: #e6e3df;
    --card-light: #f4f5f6;
    --card-mid: #dfe3e7;
    --card-warm: #e8d9d2;
    --ink: #1c231f;
    --band: #161c18;
    --band-soft: #2a322d;
    --icon-light: #d9d9d9;
  }
  * { margin: 0; padding: 0; box-sizing: border-box; }
  html, body {
    width: 1200px; height: 970px; overflow: hidden;
    background: var(--canvas);
    font-family: "Poppins", sans-serif;
  }
  .card {
    position: absolute; left: 100px; top: 200px;
    width: 1000px; height: 570px;
    border-radius: 26px; overflow: hidden;
    background:
      radial-gradient(ellipse 40% 30% at 28% 70%, var(--card-warm), transparent 70%),
      linear-gradient(160deg, var(--card-light) 0%, var(--card-mid) 55%, #d4d6d6 100%);
    box-shadow: 0 18px 40px rgba(0,0,0,0.18);
  }
  .card-shapes { position: absolute; inset: 0; }
  .brand-name {
    position: absolute; left: 100px; top: 222px; width: 350px;
    text-align: center;
    font-weight: 700; font-size: 74px; letter-spacing: -1px;
    color: var(--ink); line-height: 1;
  }
  .divider {
    position: absolute; left: 499px; top: 182px;
    width: 3px; height: 162px; background: var(--ink);
  }
  .holder { position: absolute; left: 553px; top: 172px; color: var(--ink); }
  .holder-name { font-weight: 700; font-size: 28px; line-height: 1.1; letter-spacing: 0.2px; }
  .holder-title { font-weight: 400; font-size: 22px; line-height: 1.2; }
  .contact-list { list-style: none; margin-top: 24px; }
  .contact-item {
    display: flex; align-items: center; gap: 14px;
    font-size: 23px; font-weight: 400; line-height: 30px;
  }
  .contact-icon { width: 18px; height: 18px; flex: none; }
  .social-list {
    position: absolute; left: 805px; top: 486px;
    display: flex; gap: 20px;
  }
  .social-dot {
    width: 34px; height: 34px; border-radius: 6px;
    background: var(--icon-light);
  }
</style>
</head>
<body>
  <div class="card">
    <svg class="card-shapes" viewBox="0 0 1000 570" width="1000" height="570" aria-hidden="true">
      <path class="band" fill="var(--band)"
        d="M0,452 C200,500 350,540 500,530 C650,520 800,440 1000,436 L1000,570 L0,570 Z"/>
      <path class="swoosh" fill="var(--band-soft)"
        d="M45,452 C250,520 480,545 690,478 C800,444 900,422 950,420 C880,425 790,448 680,494 C480,566 250,525 45,452 Z"/>
    </svg>

    <div class="brand-name">THRUM</div>
    <div class="divider"></div>

    <div class="holder">
      <div class="holder-name">NORA J. ELLIS</div>
      <div class="holder-title">Director</div>
      <ul class="contact-list">
        <li class="contact-item">
          <svg class="contact-icon" viewBox="0 0 24 24"><path fill="var(--ink)" d="M6.6 10.8a15 15 0 0 0 6.6 6.6l2.2-2.2a1 1 0 0 1 1-.25 11.4 11.4 0 0 0 3.6.57 1 1 0 0 1 1 1V20a1 1 0 0 1-1 1A17 17 0 0 1 3 4a1 1 0 0 1 1-1h3.5a1 1 0 0 1 1 1c0 1.25.2 2.45.57 3.57a1 1 0 0 1-.25 1z"/></svg>
          +1 555 -013-2048
        </li>
        <li class="contact-item">
          <svg class="contact-icon" viewBox="0 0 24 24"><rect x="2" y="5" width="20" height="14" fill="var(--ink)"/><path d="M2 5l10 8 10-8" fill="none" stroke="#fff" stroke-width="1.6"/></svg>
          team@thrum.com
        </li>
        <li class="contact-item">
          <svg class="contact-icon" viewBox="0 0 24 24"><circle cx="12" cy="12" r="10" fill="var(--ink)"/><path d="M2 12h20M12 2v20M12 2c-4 4-4 16 0 20M12 2c4 4 4 16 0 20" fill="none" stroke="#fff" stroke-width="1"/></svg>
          www.THRUM.com
        </li>
      </ul>
    </div>

    <div class="social-list">
      <span class="social-dot"></span>
      <span class="social-dot"></span>
      <span class="social-dot"></span>
    </div>
  </div>
</body>
</html>
```